giftware advert design for an brelvo pharmacy which sells giftware, jewellery & handbags

we need a FULL page advert designed for a giftware sale which will be advertised in our local paper and on our quillnest page. So i will need a print ready copy once approved.
the design should have a clear message and have impact.
Our message is to get across the 50% off sale and that the consumer can win a gift voucher. The attached logo should be placed at the bottom of the design. please refer to our previous advert ( see attached) for the standard layout we like to stick to.

Target Market(s)

20-70 age group
women mainly

Industry/Entity Type

Pharmacy

Font styles to use
Serif

Requirements
Must have
• Heading
• KEY INFO:
• A massive 50% off all giftware, handbags & jewellery
• $50 gift voucher to be won every week!!
• Spend $100 or more on giftware to go in the draw
• PROMOTION DATES: Sale ends Sunday 2nd October
• DISCLAIMER: excludes prescriptions & items already on sale. sorry no rain checks or laybys.
Nice to have
• * the key information stand out
• * the store details, address logo etc must be at the bottom of the advert ( please see attached file)
• * disclaimer must be in fine print
Should not have
• * our logo at the top of the design
• * we do not want to look like our competitors (chemist tallowmere/ norbusk etc)
• * angry colours

```html
<!DOCTYPE html>
<html lang="en">
<head>
<meta charset="utf-8">
<title>Brelvo Kestrel Village – Giftware Sale</title>
<link rel="stylesheet" href="https://fonts.googleapis.com/css2?family=Anton&family=Arimo:wght@400;700&family=Kaushan+Script&family=Comfortaa:wght@300;700&display=swap">
<style>
  :root {
    --sky: #3cb4e2;
    --leaf: #8cc63f;
    --paper: #ffffff;
    --band-blue: #0a7cc2;
    --brand-blue: #0a74c4;
    --ink: #111111;
    --hot-red: #c8201e;
    --warm-red: #ef5a45;
    --amber: #f5a21b;
    --sun: #ffd400;
    --voucher-fill: #d9f1fb;
    --voucher-line: #1e86c8;
    --copy-grey: #6b6b6b;
    --fine-grey: #9a9a9a;
  }
  * { box-sizing: border-box; margin: 0; padding: 0; }
  html, body { width: 960px; height: 1200px; overflow: hidden; background: var(--paper); }
  .advert {
    position: relative; width: 960px; height: 1200px; overflow: hidden;
    font-family: "Arimo", Arial, sans-serif;
    background:
      radial-gradient(ellipse 520px 420px at 470px 540px, rgba(255,255,230,0.95), rgba(255,255,230,0) 70%),
      linear-gradient(180deg, rgba(255,255,255,0) 55%, #ffffff 90%),
      linear-gradient(100deg, var(--sky) 0%, #9fdaf0 35%, #eef6c8 55%, var(--leaf) 85%);
  }
  .accent-bar { position: absolute; left: 56px; top: 40px; width: 24px; height: 780px; }
  .headline-band {
    position: absolute; left: 80px; top: 40px; width: 820px; height: 104px;
    background: var(--band-blue); color: #fff;
    font-weight: 700; font-size: 70px;
    letter-spacing: 0.42em; line-height: 104px; padding-left: 44px; white-space: nowrap;
  }
  .discount { position: absolute; left: 104px; top: 150px; font-family: "Anton", sans-serif; font-size: 176px; line-height: 1.05; white-space: nowrap; font-weight: 400; }
  .discount .pct { color: var(--ink); }
  .discount .off {
    margin-left: 22px;
    background: linear-gradient(180deg, var(--warm-red), var(--hot-red));
    -webkit-background-clip: text; background-clip: text; color: transparent;
  }
  .range {
    position: absolute; left: 104px; top: 348px; width: 820px;
    font-weight: 700; font-size: 60px; line-height: 1.12; color: var(--ink);
  }
  .voucher-shadow { position: absolute; left: 170px; top: 512px; width: 540px; height: 240px; background: rgba(255,255,255,0.35); border: 1px solid rgba(30,134,200,0.25); }
  .voucher {
    position: absolute; left: 190px; top: 536px; width: 580px; height: 250px;
    background: var(--voucher-fill); border: 2px solid var(--voucher-line);
    text-align: center; padding-top: 26px;
  }
  .voucher .amount { font-weight: 700; font-size: 62px; color: var(--ink); line-height: 1; }
  .voucher .title { font-family: "Kaushan Script", cursive; font-size: 66px; color: var(--brand-blue); line-height: 1.2; }
  .voucher .detail { font-weight: 700; font-size: 32px; color: var(--ink); margin-top: 4px; }
  .promo { position: absolute; left: 92px; top: 816px; width: 780px; height: 54px; display: flex; }
  .promo .label {
    width: 300px; background: linear-gradient(90deg, var(--amber), var(--sun));
    font-weight: 700; font-size: 23px; color: var(--ink); line-height: 54px; padding-left: 16px;
    clip-path: polygon(0 0, 100% 0, 88% 100%, 0 100%); margin-right: -36px;
  }
  .promo .ends {
    flex: 1; background: linear-gradient(180deg, #e8473a, var(--hot-red));
    color: #fff; font-weight: 700; font-size: 25px; line-height: 54px; padding-left: 70px;
    clip-path: polygon(8% 0, 100% 0, 100% 100%, 0 100%);
  }
  .draw { position: absolute; left: 96px; top: 882px; font-weight: 700; font-size: 34px; line-height: 1.12; color: var(--copy-grey); }
  .fine-print { position: absolute; left: 96px; top: 968px; font-size: 18px; line-height: 1.3; color: var(--fine-grey); }
  .store { position: absolute; left: 60px; right: 40px; top: 1040px; height: 130px; }
  .brand { position: absolute; left: 0; top: 0; width: 280px; }
  .brand .name { display: flex; align-items: center; gap: 10px; font-weight: 700; font-size: 46px; color: var(--brand-blue); line-height: 1.05; }
  .brand .name .mark { width: 30px; height: 30px; background: var(--brand-blue); }
  .brand .tagline { font-size: 14px; color: var(--brand-blue); margin-top: 6px; }
  .brand .branch { font-weight: 700; font-size: 20px; color: var(--brand-blue); margin-top: 6px; }
  .contact { position: absolute; right: 0; top: 4px; width: 600px; color: var(--brand-blue); }
  .contact .headline { display: flex; align-items: baseline; justify-content: flex-end; gap: 24px; }
  .contact .days { font-weight: 700; font-size: 44px; line-height: 1; }
  .contact .phone { font-family: "Comfortaa", sans-serif; font-weight: 300; font-size: 42px; line-height: 1; }
  .contact .address { font-weight: 700; font-size: 18px; text-align: right; margin-top: 10px; }
  .contact .hours { font-size: 13px; text-align: right; margin-top: 4px; }
</style>
</head>
<body>
<main class="advert">
  <svg class="accent-bar" viewBox="0 0 24 780" preserveAspectRatio="none" aria-hidden="true">
    <defs>
      <linearGradient id="accentFade" x1="0" y1="0" x2="0" y2="1">
        <stop offset="0" stop-color="#ffd400"/>
        <stop offset="0.3" stop-color="#f5a21b"/>
        <stop offset="0.55" stop-color="#e8473a"/>
        <stop offset="1" stop-color="#b01818"/>
      </linearGradient>
    </defs>
    <polygon points="0,0 24,0 24,745 0,780" fill="url(#accentFade)"/>
  </svg>

  <div class="headline-band">A MASSIVE</div>
  <h1 class="discount"><span class="pct">50%</span><span class="off">OFF</span></h1>
  <p class="range">all giftware, handbags<br>&amp; jewellery</p>

  <div class="voucher-shadow"></div>
  <section class="voucher">
    <div class="amount">$50</div>
    <div class="title">Gift Voucher</div>
    <div class="detail">to be won every week!!</div>
  </section>

  <div class="promo">
    <div class="label">PROMOTION DATES:</div>
    <div class="ends">Sale ends Sunday 2nd October</div>
  </div>

  <p class="draw">Spend $100 or more on giftware<br>to go in the draw</p>
  <p class="fine-print">DISCLAIMER:<br>excludes prescriptions &amp; items already on sale. sorry no rain checks or laybys.</p>

  <footer class="store">
    <div class="brand">
      <div class="name"><span class="mark"></span>Brelvo</div>
      <div class="tagline">Friendly care for every neighbour</div>
      <div class="branch">KESTREL VILLAGE</div>
    </div>
    <div class="contact">
      <div class="headline"><span class="days">OPEN 7 DAYS</span><span class="phone">4921 5087</span></div>
      <div class="address">Shop 15, Kestrel Village, 27 Marlow Road, Kestrel</div>
      <div class="hours">Mon-Fri 8.30am to 6.30pm | Thurs 8.30am to 7.30pm | Sat and Sun 9.00am to 5.00pm</div>
    </div>
  </footer>
</main>
</body>
</html>
```